Thank you for shopping with us business card

We would like a thank you card for our rebranded business. We used to be "Brindle Goods" but are now "Marlow Finds. Old thank you card and new logo will be attached for reference. New thank you card does not have to be same design as old thank you card, but please use new logo.
Shopmart URL is now marlowfinds.shopmart.example
Instagram is @Marlow_Finds
Email is marlowfinds@mailbox.example
Thank you!

Contact Information for Business Card

Shopmart site, email, Instagram

```html
<!DOCTYPE html>
<html lang="en">
<head>
<meta charset="utf-8">
<title>Marlow Finds – Thank You Card</title>
<link rel="stylesheet" href="https://fonts.googleapis.com/css2?family=Montserrat:wght@500;600&family=Quicksand:wght@400;500&display=swap">
<style>
  :root {
    --backdrop: #2b2b2b;
    --card: #ffffff;
    --ink: #111111;
    --ink-soft: #2a2a2a;
  }
  * { margin: 0; padding: 0; box-sizing: border-box; }
  html, body { width: 1200px; height: 900px; overflow: hidden; background: var(--backdrop); }
  .canvas { position: relative; width: 1200px; height: 900px; }
  .card {
    position: absolute; left: 280px; width: 640px; height: 366px;
    background: var(--card); color: var(--ink);
  }
  .card--back { top: 60px; }
  .card--front { top: 470px; }

  .brand-mark { position: absolute; width: 58px; height: 58px; background: var(--ink); }
  .brand-mark-name {
    position: absolute; font-family: "Montserrat", sans-serif; font-weight: 600;
    font-size: 13px; line-height: 1.25; letter-spacing: 0.04em; text-transform: uppercase; color: var(--ink);
  }
  .divider { position: absolute; width: 2px; background: var(--ink); }

  /* back side */
  .card--back .brand-mark { left: 120px; top: 82px; }
  .card--back .brand-mark-name { left: 100px; top: 150px; width: 100px; text-align: center; }
  .card--back .divider { left: 238px; top: 58px; height: 140px; }
  .message { position: absolute; left: 264px; top: 66px; width: 330px; }
  .message-title {
    font-family: "Montserrat", sans-serif; font-weight: 600; font-size: 15px;
    letter-spacing: 0.03em; text-transform: uppercase; margin-bottom: 12px;
  }
  .message-body {
    font-family: "Quicksand", sans-serif; font-weight: 500; font-size: 15px;
    line-height: 1.6; letter-spacing: 0.04em; color: var(--ink-soft);
  }
  .rule { position: absolute; left: 54px; right: 54px; height: 1.5px; background: var(--ink); }
  .rule--top { top: 234px; }
  .rule--bottom { top: 302px; }
  .contacts {
    position: absolute; left: 54px; right: 54px; top: 234px; height: 68px;
    display: flex; align-items: center; justify-content: space-between;
    font-family: "Quicksand", sans-serif; font-weight: 500; font-size: 12px; color: var(--ink-soft);
  }
  .contact { display: flex; align-items: center; gap: 5px; white-space: nowrap; }
  .contact-icon { width: 12px; height: 12px; border-radius: 50%; background: var(--ink); flex: none; }
  .separator { flex: none; padding: 0 4px; color: var(--ink-soft); }

  /* front side */
  .card--front .brand-mark { left: 196px; top: 144px; width: 66px; height: 66px; }
  .card--front .divider { left: 296px; top: 118px; height: 120px; }
  .wordmark {
    position: absolute; left: 322px; top: 134px;
    font-family: "Montserrat", sans-serif; font-weight: 600; font-size: 36px;
    line-height: 1.05; letter-spacing: 0.01em; text-transform: uppercase; color: var(--ink);
  }
</style>
</head>
<body>
<main class="canvas">
  <section class="card card--back" aria-label="Thank you card, back">
    <div class="brand-mark" aria-hidden="true"></div>
    <span class="brand-mark-name">Marlow Finds</span>
    <div class="divider"></div>
    <div class="message">
      <h1 class="message-title">Thank you for your purchase</h1>
      <p class="message-body">Your Purchase Made My Day And<br>I Hope This Package Brightens Your.<br>Please Come Back And Leave A Review!</p>
    </div>
    <div class="rule rule--top"></div>
    <div class="contacts">
      <span class="contact"><span class="contact-icon"></span>marlowfinds.shopmart.example</span>
      <span class="separator">|</span>
      <span class="contact"><span class="contact-icon"></span>@Marlow_Finds</span>
      <span class="separator">|</span>
      <span class="contact"><span class="contact-icon"></span>marlowfinds@mailbox.example</span>
    </div>
    <div class="rule rule--bottom"></div>
  </section>

  <section class="card card--front" aria-label="Thank you card, front">
    <div class="brand-mark" aria-hidden="true"></div>
    <div class="divider"></div>
    <h2 class="wordmark">Marlow<br>Finds</h2>
  </section>
</main>
</body>
</html>
```